Maplecrest Counseling and Consulting, LLC

We need a business card and stationary designed for a new therapy practice for Laura Whitcombe. Laura Whitcombe is a Therapist who specializes in Therapy for children dealing with trauma and/or stress. Below are some of her thoughts:
colors can include purple, blue, turquoise and green (does NOT have to be all colors) See attached Logos
Laura Whitcombe, LMHC
Maplecrest Counseling & Counseling Inc.
4382 W. Harbor Parkway
Suite 714
Boca Raton, FL 33912
Phone: 561-730-2254
Fax: 561-730-2255
Email: laura@maplecrestcc-example.com
Website: www.maplecrestcc-example.com

```html
<!DOCTYPE html>
<html lang="en">
<head>
<meta charset="utf-8">
<title>Maplecrest Counseling – Business Card Concepts</title>
<link rel="stylesheet" href="https://fonts.googleapis.com/css2?family=Source+Sans+3:wght@400&family=Tinos&display=swap">
<style>
  :root {
    --page: #ffffff;
    --ink: #111111;
    --card-border: #333333;
    --lavender: #c4c0e0;
    --mark-grey: #7c7c7c;
    --faint: #d6dcc8;
    --sans: "Source Sans 3", "Myriad Pro", Arial, sans-serif;
    --serif: "Tinos", "Times New Roman", serif;
  }
  * { margin: 0; padding: 0; box-sizing: border-box; }
  html, body { width: 873px; height: 1200px; overflow: hidden; background: var(--page); }
  .sheet { position: relative; width: 873px; height: 1200px; }

  .card { position: absolute; border: 1.5px solid var(--card-border); background: var(--page); overflow: hidden; }
  .card--classic { left: 22px; top: 45px; width: 718px; height: 357px; }
  .card--watermark { left: 22px; top: 440px; width: 692px; height: 360px; }
  .card--lavender { left: 22px; top: 834px; width: 701px; height: 329px; background: var(--lavender); border-color: #555; }

  .abs { position: absolute; white-space: nowrap; }
  .centered { transform: translateX(-50%); text-align: center; }
  h1, h2 { font-weight: 400; }

  /* Brand block: plain circle plus the practice name in body type */
  .brand-dot { position: absolute; border-radius: 50%; background: var(--mark-grey); }
  .brand { position: absolute; font-family: var(--sans); font-weight: 400; color: var(--ink); text-align: center; line-height: 1.2; white-space: nowrap; transform: translateX(-50%); }
  .brand-name { display: block; font-size: 30px; }
  .brand-sub { display: block; font-size: 14px; }

  .person { font-family: var(--sans); font-weight: 400; color: var(--ink); }
  .contact { font-family: var(--sans); color: var(--ink); line-height: 1.3; }

  /* Card 1 */
  .card--classic .brand-dot { left: 70px; top: 22px; width: 90px; height: 90px; }
  .card--classic .brand { left: 115px; top: 128px; }
  .card--classic .person { left: 439px; top: 55px; font-size: 30px; }
  .card--classic .contact { left: 439px; top: 113px; font-size: 19px; }
  .card--classic .contact-web { left: 439px; top: 240px; font-size: 19px; }

  /* Card 2 */
  .card--watermark .brand-dot { left: 360px; top: 40px; width: 150px; height: 150px; background: #e6e6e6; }
  .card--watermark .faint-brand { left: 300px; top: 215px; font-family: var(--serif); color: var(--faint); text-align: center; line-height: 1.05; transform: translateX(-50%); }
  .card--watermark .faint-brand .faint-name { display: block; font-size: 76px; }
  .card--watermark .faint-brand .faint-sub { display: block; font-size: 28px; }
  .card--watermark .person { left: 330px; top: 18px; font-family: var(--serif); font-size: 33px; }
  .card--watermark .contact { left: 330px; top: 90px; font-family: var(--serif); font-size: 24px; line-height: 1.34; }
  .card--watermark .contact-web { left: 330px; top: 250px; font-family: var(--serif); font-size: 24px; line-height: 1.34; color: var(--ink); }

  /* Card 3 */
  .card--lavender .brand-dot { left: 108px; top: 40px; width: 90px; height: 90px; }
  .card--lavender .brand { left: 153px; top: 146px; }
  .card--lavender .address { left: 128px; top: 228px; font-family: var(--serif); font-size: 17px; line-height: 1.4; color: var(--ink); }
  .card--lavender .person { left: 473px; top: 76px; font-size: 34px; }
  .card--lavender .contact-web { left: 473px; top: 128px; font-size: 21px; line-height: 1.4; }
</style>
</head>
<body>
<main class="sheet">

  <section class="card card--classic" aria-label="Business card, white layout">
    <span class="brand-dot" aria-hidden="true"></span>
    <div class="brand"><span class="brand-name">Maplecrest</span><span class="brand-sub">Counseling and Consulting, Inc.</span></div>
    <h1 class="abs centered person">Laura Whitcombe, LMHC</h1>
    <p class="abs centered contact">4382 W. Harbor Parkway<br>Suite 714 Boca Raton, FL 33912<br>Phone: 561-730-2254<br>Fax: 561-730-2255</p>
    <p class="abs centered contact contact-web">Email: laura@maplecrestcc-example.com<br>Website: www.maplecrestcc-example.com</p>
  </section>

  <section class="card card--watermark" aria-label="Business card, faint brand background">
    <span class="brand-dot" aria-hidden="true"></span>
    <div class="abs faint-brand" aria-hidden="true"><span class="faint-name">Maplecrest</span><span class="faint-sub">Counseling and Consulting, Inc.</span></div>
    <h2 class="abs centered person">Laura Whitcombe, LMHC</h2>
    <p class="abs centered contact">4382 W. Harbor Parkway<br>Suite 714 Boca Raton, FL 33912<br>Phone: 561-730-2254<br>Fax: 561-730-2255</p>
    <p class="abs centered contact-web">Email: laura@maplecrestcc-example.com<br>Website: www.maplecrestcc-example.com</p>
  </section>

  <section class="card card--lavender" aria-label="Business card, lavender layout">
    <span class="brand-dot" aria-hidden="true"></span>
    <div class="brand"><span class="brand-name">Maplecrest</span><span class="brand-sub">Counseling and Consulting, Inc.</span></div>
    <p class="abs centered address">4382 W. Harbor Parkway<br>Suite 714 Boca Raton, FL 33912<br>Phone: 561-730-2254<br>Fax: 561-730-2255</p>
    <h2 class="abs centered person">Laura Whitcombe, LMHC</h2>
    <p class="abs centered contact-web person">Email: laura@maplecrestcc-example.com<br>Website: www.maplecrestcc-example.com</p>
  </section>

</main>
</body>
</html>
```